Torvanex needs a Monthly Newsletter

We need a newsletter design for a company located in Sydney Australia. We are an IT Services and Software Development company with both arms separated as a business. We would like to see designs that follow the same elements that our website has being www.torvanex.com.au.
It needs an element of our corporate blue logo in it and would like the same colour elements included throughout the file.
The file needs to be MailChimp compatible and we would need all the files being HTML, the graphics, the PSD files, the MailChimp ready file, etc.

```html
<!DOCTYPE html>
<html lang="en">
<head>
<meta charset="utf-8">
<title>Torvanex Monthly Newsletter</title>
<link rel="stylesheet" href="https://fonts.googleapis.com/css2?family=Arimo:wght@400;700&display=swap">
<style>
  :root {
    --page-bg: #ebebeb;
    --brand-blue: #2f86e0;
    --brand-blue-light: #5eaaf5;
    --divider-teal: #2bb3c9;
    --white: #ffffff;
    --heading: #333333;
    --body-text: #a3a3a3;
    --hero-light: #eef0f2;
    --hero-dark: #9ea3a8;
    --icon-ring: #bcdcf8;
  }
  * { box-sizing: border-box; margin: 0; padding: 0; }
  html, body {
    width: 706px; height: 1200px; overflow: hidden;
    background: var(--page-bg);
    font-family: "Arimo", Arial, sans-serif;
  }
  .newsletter {
    position: absolute; left: 31px; top: 0;
    width: 632px; height: 1200px;
    display: flex;
  }
  /* Sidebar */
  .sidebar {
    width: 214px; height: 100%;
    background: var(--brand-blue);
    color: var(--white);
  }
  .view-online {
    height: 73px; border-bottom: 1px solid var(--divider-teal);
    text-align: center; font-size: 12px; line-height: 15px; padding-top: 22px;
  }
  .view-online a { color: var(--white); text-decoration: underline; }
  .brand {
    height: 90px; border-bottom: 1px solid var(--divider-teal);
    display: flex; align-items: center; gap: 8px; padding-left: 29px;
  }
  .brand-mark { width: 30px; height: 30px; border-radius: 50%; background: var(--white); }
  .brand-name { font-size: 22px; font-weight: 700; letter-spacing: 0.5px; color: var(--white); }
  .main-nav {
    height: 195px; border-bottom: 1px solid var(--divider-teal);
    list-style: none; padding: 26px 0 0 31px;
  }
  .main-nav li {
    display: flex; align-items: center; gap: 13px;
    height: 36px; font-size: 12px; font-weight: 700;
  }
  .nav-icon {
    width: 25px; height: 25px; border-radius: 50%;
    background: var(--white); border: 2px solid var(--icon-ring);
    display: flex; align-items: center; justify-content: center;
  }
  .nav-icon svg { width: 12px; height: 12px; fill: #5a6673; }
  .contact { padding: 30px 0 0 29px; }
  .contact h2 { font-size: 17px; font-weight: 700; margin-bottom: 6px; }
  .contact p { font-size: 12px; line-height: 17.5px; }
  .social { display: flex; gap: 5px; margin-top: 9px; list-style: none; }
  .social li {
    width: 24px; height: 24px; border-radius: 50%;
    background: var(--white); border: 2px solid var(--icon-ring);
  }
  /* Content */
  .content {
    width: 418px; height: 100%;
    background: var(--white);
    border-right: 1px solid #d6d6d6;
  }
  .hero {
    height: 200px;
    background: linear-gradient(120deg, var(--hero-dark) 0%, #c9cdd1 30%, var(--hero-light) 60%, #f8f9fa 100%);
  }
  .article {
    border-top: 1px solid #f0f0f0;
    background: linear-gradient(180deg, #f6f6f6 0, var(--white) 14px);
    padding: 0 16px;
  }
  .article h2 { font-size: 17px; font-weight: 700; color: var(--heading); }
  .article p { font-size: 12px; line-height: 17.5px; color: var(--body-text); }
  .article p + p { margin-top: 17.5px; }
  .feature { height: 178px; border-top: none; background: var(--white); padding: 28px 15px 0; }
  .feature h2 { font-size: 18px; margin-bottom: 6px; }
  .more-link {
    display: block; width: 54px; height: 25px; margin: 9px 0 0 auto;
    background: var(--brand-blue); color: var(--white);
    border-radius: 4px; font-size: 12px; line-height: 25px; text-align: center;
    text-decoration: none;
  }
  .story { height: 198px; padding-top: 23px; }
  .story h2 { margin-bottom: 6px; }
  .story.short { height: 196px; }
  .decide {
    height: 148px; text-align: center; padding-top: 28px;
    border-top: 1px solid #f0f0f0;
    background: linear-gradient(180deg, #f6f6f6 0, var(--white) 14px);
  }
  .decide h2 { font-size: 17px; font-weight: 700; color: var(--brand-blue); }
  .decide p { font-size: 12px; color: var(--body-text); margin-top: 7px; }
  .decide-button {
    display: inline-block; margin-top: 11px;
    width: 141px; height: 41px; border-radius: 5px;
    background: linear-gradient(180deg, var(--brand-blue-light), var(--brand-blue));
    border: 1px solid #2a78c9;
    color: var(--white); font-size: 14px; font-weight: 700; line-height: 39px;
    text-decoration: none;
  }
  .site-footer {
    height: 83px; text-align: center; padding-top: 25px;
    border-top: 1px solid #f0f0f0;
    background: linear-gradient(180deg, #f6f6f6 0, var(--white) 14px);
    font-size: 12px; color: #777777;
  }
  .site-footer a { color: #555555; text-decoration: underline; }
  .site-footer .copyright { color: var(--brand-blue); margin-top: 8px; }
</style>
</head>
<body>
<div class="newsletter">
  <aside class="sidebar">
    <div class="view-online">You can't see this email?<br><a href="#">View Online</a></div>
    <div class="brand"><span class="brand-mark"></span><span class="brand-name">TORVANEX</span></div>
    <ul class="main-nav">
      <li><span class="nav-icon"><svg viewBox="0 0 12 12"><path d="M6 1 0.5 6H2v5h3V8h2v3h3V6h1.5z"/></svg></span>Home</li>
      <li><span class="nav-icon"><svg viewBox="0 0 12 12"><circle cx="6" cy="3.5" r="2.6"/><path d="M1 11.5c0-3 2.2-4.5 5-4.5s5 1.5 5 4.5z"/></svg></span>About Us</li>
      <li><span class="nav-icon"><svg viewBox="0 0 12 12"><path d="M1 3.5h3l1-1.5h2l1 1.5h3V10H1z"/><circle cx="6" cy="6.6" r="2" fill="#fff"/></svg></span>Cloud</li>
      <li><span class="nav-icon"><svg viewBox="0 0 12 12"><path d="M5 0.5h2l.3 1.6 1.3.6 1.4-.9 1.4 1.4-.9 1.4.6 1.3 1.6.3v2l-1.6.3-.6 1.3.9 1.4-1.4 1.4-1.4-.9-1.3.6-.3 1.6H5l-.3-1.6-1.3-.6-1.4.9-1.4-1.4.9-1.4-.6-1.3L0.5 7V5l1.6-.3.6-1.3-.9-1.4 1.4-1.4 1.4.9 1.3-.6z"/><circle cx="6" cy="6" r="1.8" fill="#fff"/></svg></span>IT Service</li>
    </ul>
    <div class="contact">
      <h2>Contact Details</h2>
      <p>Suite 12, level 4<br>42-44 Harlow Street<br>Kestrel Bay NSW 2477<br>info@torvanex.au<br>SALES 1300 555 214<br>SUPPORT 02 5550 1420</p>
      <ul class="social" aria-label="Social links">
        <li></li><li></li><li></li><li></li><li></li>
      </ul>
    </div>
  </aside>

  <main class="content">
    <div class="hero" role="img" aria-label="Close-up photo of calculator keys beside a printed monthly spreadsheet"></div>

    <section class="article feature">
      <h2>What's new in Torvanex</h2>
      <p>Lorem Ipsum is simply dummy text of the printing and typesetting industry. Lorem Ipsum has been the industry's standard It has survived not only five centuries, but also the leap into electronic typesetting, remaining essentially unchanged...</p>
      <a class="more-link" href="#">More+</a>
    </section>

    <section class="article story">
      <h2>Did You Know?</h2>
      <p>Lorem Ipsum has been the industry's standard It has survived not only five centuries, but also the leap into electronic.</p>
      <p>Lorem Ipsum is simply dummy text of the printing and typesetting industry. Lorem Ipsum has been the industry's standard It has survived not only five centuries, but also the leap into electronic typesetting, remaining essentially unchanged...</p>
    </section>

    <section class="article story short">
      <h2>Case Studies</h2>
      <p>Lorem Ipsum has been the industry's standard It has survived not only five centuries, but also the leap into electronic.</p>
      <p>Lorem Ipsum is simply dummy text of the printing and typesetting industry. Lorem Ipsum has been the industry's standard It has survived not only five centuries, but also the leap into electronic typesetting, remaining essentially unchanged...</p>
    </section>

    <section class="article story short">
      <h2>New Technologies</h2>
      <p>Lorem Ipsum has been the industry's standard It has survived not only five centuries, but also the leap into electronic.</p>
      <p>Lorem Ipsum is simply dummy text of the printing and typesetting industry. Lorem Ipsum has been the industry's standard It has survived not only five centuries, but also the leap into electronic typesetting, remaining essentially unchanged...</p>
    </section>

    <section class="decide">
      <h2>Can't Decide?</h2>
      <p>Still haven't find us what you're looking for?</p>
      <a class="decide-button" href="#">Help me decide</a>
    </section>

    <footer class="site-footer">
      <p>If you no longer wish to receive emails please <a href="#">unsubscribe</a></p>
      <p class="copyright">Copyright © 2012 torvanex.com</p>
    </footer>
  </main>
</div>
</body>
</html>
```